Online Psychology Practice needs business cards.

Online Psychology service needs business cards. Have own logo- please see uploaded. I have other file formats if you need (not sure one needed?)

Details for Business Card:
Fiona Kettlewood
Clinical Psychologist BPsych, BPsych (Hons), MPsych (Clin), MAPS
T: 0457260714 | F: 08 71526804
E: hello@harbourlightmindcarestudio.com.au
W: harbourlightmindcarestudio.com.au

Industry/Entity Type

Health

Contact Information for Business Card

Logo plus details above (couldn't write in this section)

```html
<!DOCTYPE html>
<html lang="en">
<head>
<meta charset="utf-8">
<title>Harbourlight Mindcare Studio – Business Card</title>
<link href="https://fonts.googleapis.com/css2?family=Arimo:wght@400;700&display=swap" rel="stylesheet">
<style>
  :root {
    --backdrop: #262626;
    --navy: #1b5a82;
    --teal: #168ba8;
    --white: #ffffff;
    --paper: #ffffff;
  }
  html, body {
    margin: 0;
    padding: 0;
    width: 1200px;
    height: 1059px;
    overflow: hidden;
    background: var(--backdrop);
    font-family: "Arimo", Arial, sans-serif;
  }
  .canvas {
    position: relative;
    width: 1200px;
    height: 1059px;
  }
  .card {
    position: absolute;
    left: 255px;
    width: 690px;
    height: 392px;
    border-radius: 20px;
    overflow: hidden;
  }
  .card--front { top: 89px; background: var(--paper); }
  .card--back { top: 538px; background: var(--navy); }

  .front-wave { position: absolute; inset: 0; }

  .brand {
    position: absolute;
    text-align: center;
    font-family: "Arimo", Arial, sans-serif;
    font-weight: 700;
    text-transform: uppercase;
  }
  .brand__dot { display: block; margin: 0 auto; border-radius: 50%; }
  .brand--front { right: 30px; top: 40px; width: 200px; color: var(--navy); }
  .brand--front .brand__dot { width: 52px; height: 52px; background: var(--navy); margin-bottom: 12px; }
  .brand--front .brand__name { font-size: 21px; line-height: 1.15; letter-spacing: 1.5px; }

  .brand--back { left: 0; right: 0; top: 92px; color: var(--white); }
  .brand--back .brand__dot { width: 110px; height: 110px; background: var(--white); margin-bottom: 22px; }
  .brand--back .brand__name { font-size: 32px; line-height: 1.15; letter-spacing: 2.5px; }

  .person {
    position: absolute;
    left: 31px;
    top: 193px;
    color: var(--white);
  }
  .person__name {
    margin: 0 0 6px;
    font-size: 24px;
    font-weight: 700;
    color: var(--teal);
    letter-spacing: 0.3px;
  }
  .person__title {
    margin: 0;
    font-size: 15px;
    line-height: 20px;
  }
  .contact {
    list-style: none;
    margin: 16px 0 0;
    padding: 0;
    font-size: 15.5px;
    line-height: 20px;
  }
  .contact li { display: flex; align-items: center; gap: 6px; }
  .contact svg { width: 12px; height: 12px; flex: none; }
</style>
</head>
<body>
<main class="canvas">

  <section class="card card--front">
    <svg class="front-wave" viewBox="0 0 690 392" preserveAspectRatio="none" aria-hidden="true">
      <path fill="var(--teal)" d="M112,137 C260,126 430,244 565,250 C628,252 668,214 690,170 L690,392 L0,392 Z"/>
      <path fill="var(--navy)" stroke="#ffffff" stroke-width="3" d="M0,205 C40,162 90,140 140,143 C260,150 420,262 560,264 C622,265 662,240 692,203 L692,394 L-2,394 Z"/>
    </svg>

    <div class="brand brand--front">
      <span class="brand__dot"></span>
      <div class="brand__name">Harbourlight<br>Mindcare Studio</div>
    </div>

    <div class="person">
      <h1 class="person__name">FIONA KETTLEWOOD</h1>
      <p class="person__title">Clinical Psychologist BPsych,<br>BPsych (Hons), MPsych (Clin), MAPS</p>
      <ul class="contact">
        <li>
          <svg viewBox="0 0 12 12" aria-hidden="true"><path fill="var(--teal)" d="M2.5 1 L4.5 1 L5.2 3.3 L4 4.3 C4.6 5.8 6.2 7.4 7.7 8 L8.7 6.8 L11 7.5 L11 9.5 C11 10.3 10.3 11 9.5 11 C5 11 1 7 1 2.5 C1 1.7 1.7 1 2.5 1 Z"/></svg>
          0457260714
        </li>
        <li>
          <svg viewBox="0 0 12 12" aria-hidden="true"><rect fill="var(--teal)" x="3" y="1" width="6" height="3"/><rect fill="var(--teal)" x="1" y="4.5" width="10" height="4.5" rx="1"/><rect fill="var(--teal)" x="3" y="8" width="6" height="3"/></svg>
          08 71526804
        </li>
        <li>
          <svg viewBox="0 0 12 12" aria-hidden="true"><rect fill="var(--teal)" x="0.5" y="2.5" width="11" height="7"/><path fill="none" stroke="var(--navy)" stroke-width="1" d="M0.5 2.5 L6 6.5 L11.5 2.5"/></svg>
          hello@harbourlightmindcarestudio.com.au
        </li>
        <li>
          <svg viewBox="0 0 12 12" aria-hidden="true"><circle fill="var(--teal)" cx="6" cy="6" r="5.2"/><path fill="none" stroke="var(--navy)" stroke-width="0.8" d="M1 6 H11 M6 0.8 C3.5 3.5 3.5 8.5 6 11.2 M6 0.8 C8.5 3.5 8.5 8.5 6 11.2"/></svg>
          harbourlightmindcarestudio.com.au
        </li>
      </ul>
    </div>
  </section>

  <section class="card card--back">
    <div class="brand brand--back">
      <span class="brand__dot"></span>
      <div class="brand__name">Harbourlight<br>Mindcare Studio</div>
    </div>
  </section>

</main>
</body>
</html>
```